Brand new website for global research and investment startup

We need a simple website, maybe 3 pages: landing page with business description, investment philosophy, team and contact info.
We have a logo already that can be incorporated. Please use the logo only, not the text
We like the color green, something along the lines of #3D6C32 as the main color.
We'd like to design the website with geometric shapes in gradations of the base color. The shapes should suggest "work in progress", "built to last (a long time)", "solidity" and "indestructibility". One idea floating in my head sees smaller features with icosahedron and dodecahedron shapes, and maybe larger structures like crystal lattices; but please feel free to be creative and imagine your own.

```html
<!DOCTYPE html>
<html lang="en">
<head>
<meta charset="utf-8">
<title>Aldercrest — Research notes</title>
<link href="https://fonts.googleapis.com/css2?family=Gelasio:wght@400;500&family=Inter:wght@400;500;600;700&display=swap" rel="stylesheet">
<style>
:root{
  --green:#3d6c32;
  --green-bright:#5aa84a;
  --green-deep:#2d5a2e;
  --green-darker:#1e4a2f;
  --footer:#122b22;
  --ink:#1c2a22;
  --muted:#5d6761;
  --band:#f2f7f1;
  --line:#e4e8e4;
  --white:#ffffff;
}
*{margin:0;padding:0;box-sizing:border-box}
html,body{width:1200px;height:857px;overflow:hidden;background:var(--white)}
body{font-family:"Inter",sans-serif;color:var(--ink);position:relative}
.site-header{position:absolute;top:0;left:0;width:1200px;height:40px;border-bottom:1px solid var(--line);background:var(--white)}
.brand{position:absolute;left:34px;top:11px;font-family:"Inter",sans-serif;font-weight:700;font-size:14px;color:var(--green);letter-spacing:.2px}
.main-nav{position:absolute;left:213px;top:12px;display:flex;gap:19px;font-size:8.5px;color:#3a4540}
.main-nav a{color:inherit;text-decoration:none;padding-bottom:4px}
.main-nav a.active{border-bottom:1.5px solid var(--green-bright)}
.intro-btn{position:absolute;left:557px;top:4px;width:121px;height:27px;border:1px solid var(--line);border-radius:14px;box-shadow:0 1px 3px rgba(0,0,0,.08);font-size:8.5px;font-weight:600;display:flex;align-items:center;justify-content:center;color:var(--ink)}
.hero-band{position:absolute;top:40px;left:0;width:1200px;height:39px;background:var(--band)}
.eyebrow{position:absolute;left:52px;top:146px;font-size:6.5px;font-weight:700;letter-spacing:1.5px;color:var(--green)}
.section-title{position:absolute;left:34px;top:163px;font-family:"Gelasio",serif;font-weight:400;font-size:34px;line-height:38px;letter-spacing:-.5px;color:var(--ink)}
.section-lede{position:absolute;left:320px;top:228px;width:345px;font-size:10.5px;line-height:17.4px;color:#4b5650}
.notes{position:absolute;left:34px;top:318px;display:flex;gap:13px}
.note-card{width:206px;height:158px;border:1px solid var(--line);border-radius:8px;padding:17px 17px 0;position:relative}
.note-tag{font-size:6px;font-weight:700;letter-spacing:.9px;color:var(--green-bright);margin-bottom:14px}
.note-title{font-family:"Gelasio",serif;font-weight:400;font-size:12.5px;line-height:14.6px;letter-spacing:-.2px;margin-bottom:6px}
.note-text{font-size:8px;line-height:12.8px;color:var(--muted)}
.note-link{position:absolute;left:17px;top:130px;font-size:7.2px;font-weight:700;color:var(--green)}
.cta{position:absolute;left:34px;top:525px;width:644px;height:110px;border-radius:11px;overflow:hidden;background:linear-gradient(100deg,var(--green-deep),var(--green-darker))}
.cta svg{position:absolute;left:0;top:0}
.cta-title{position:absolute;left:27px;top:26px;width:320px;font-family:"Gelasio",serif;font-weight:400;font-size:17px;line-height:20px;color:var(--white)}
.cta-sub{position:absolute;left:27px;top:72px;font-size:8.7px;color:#d3e2d3}
.cta-btn{position:absolute;left:505px;top:42px;width:112px;height:26px;background:var(--white);border-radius:4px;font-size:8px;font-weight:600;color:var(--ink);display:flex;align-items:center;justify-content:center}
.site-footer{position:absolute;left:0;top:696px;width:1200px;height:161px;background:var(--footer);color:#bfd0c4}
.footer-brand{position:absolute;left:34px;top:27px;font-weight:700;font-size:14px;color:var(--white)}
.footer-about{position:absolute;left:34px;top:68px;width:300px;font-size:7.4px;line-height:11px}
.footer-col{position:absolute;top:30px}
.footer-col h4{font-size:7.5px;font-weight:700;letter-spacing:.8px;color:var(--white);margin-bottom:10px}
.footer-col li{list-style:none;font-size:7.5px;margin-bottom:7.5px}
.footer-col p{font-size:7.2px;line-height:11.8px;width:155px}
.footer-rule{position:absolute;left:34px;top:122px;width:644px;height:1px;background:#2a4437}
.footer-legal{position:absolute;left:34px;top:135px;width:644px;display:flex;justify-content:space-between;font-size:6px;color:#879a8e}
</style>
</head>
<body>
<header class="site-header">
  <div class="brand">Aldercrest</div>
  <nav class="main-nav">
    <a class="active">Home</a><a>Philosophy</a><a>Insights</a><a>Team &amp; Contact</a>
  </nav>
  <div class="intro-btn">Request an introduction</div>
</header>
<div class="hero-band"></div>

<p class="eyebrow">SELECTED THINKING</p>
<h1 class="section-title">Research notes<br>for professional<br>investors.</h1>
<p class="section-lede">The editorial system is intentionally restrained: no stock photography, no market clichés, just clear typography, data-led thinking and geometric visual cues.</p>

<section class="notes">
  <article class="note-card">
    <p class="note-tag">INVESTMENT PROCESS</p>
    <h3 class="note-title">Why founder alignment can matter over a long holding period</h3>
    <p class="note-text">A framework for thinking about incentives, decision quality and capital allocation.</p>
    <a class="note-link">View research notes →</a>
  </article>
  <article class="note-card">
    <p class="note-tag">VALUATION</p>
    <h3 class="note-title">Exceptional business does not mean any price</h3>
    <p class="note-text">How valuation discipline protects the expected return embedded in a high-quality thesis.</p>
    <a class="note-link">View research notes →</a>
  </article>
  <article class="note-card">
    <p class="note-tag">PORTFOLIO CONSTRUCTION</p>
    <h3 class="note-title">Conviction sizing without concentration by accident</h3>
    <p class="note-text">Distinguishing deliberate concentration from hidden exposure to the same underlying value driver.</p>
    <a class="note-link">View research notes →</a>
  </article>
</section>

<section class="cta">
  <svg width="644" height="110" viewBox="0 0 644 110" aria-hidden="true">
    <circle cx="498" cy="5" r="114" fill="rgba(255,255,255,0.03)"/>
    <circle cx="498" cy="5" r="102" fill="none" stroke="rgba(255,255,255,0.06)" stroke-width="24"/>
    <circle cx="498" cy="5" r="90" fill="var(--green-darker)" opacity=".35"/>
  </svg>
  <h2 class="cta-title">Built for direct conversations, not mass-market promotion.</h2>
  <p class="cta-sub">For professional investor enquiries and introductions.</p>
  <div class="cta-btn">Start a conversation →</div>
</section>

<footer class="site-footer">
  <div class="footer-brand">Aldercrest</div>
  <p class="footer-about">Research-led investing with a long-term perspective, valuation discipline and focused portfolio construction.</p>
  <div class="footer-col" style="left:345px">
    <h4>EXPLORE</h4>
    <ul><li>Philosophy</li><li>Insights</li><li>Team &amp; Contact</li></ul>
  </div>
  <div class="footer-col" style="left:522px">
    <h4>AUDIENCE</h4>
    <p>Intended for select professional investors and direct, face-to-face engagement.</p>
  </div>
  <div class="footer-rule"></div>
  <div class="footer-legal">
    <span>© 2026. All rights reserved.</span>
    <span>Information on this site is for general information only and is not investment advice or an offer to invest.</span>
  </div>
</footer>
</body>
</html>
```